Name Card Design

Looking to create a card for my business. I am a personal stylist, my business is clothes, shoes and everything to do with looking fashion forward. I help people achieve the most polished look with cloths and grooming. I would like my card to be a reflection of my qualities which are: poise, elegance, creativity and fairness.
Things I like a simple yet expensive looking, sometimes less simple but highly creative and different catches my eye. For instance I saw a card with lace trimming at the bottom, it made me think about the business that person was in. I don't like childish designs with butterflies, trees, flowers, etc.
Here is my site www.Marta-Vosel.example for your perusal

On the card it should have the following info
Marta Vosel
personal stylist
www.Marta-Vosel.example
(+65) 482-30857
Facebook page: Ringthelook

Back of the card:
Wardrobe weeding
Personal shopping
Style consultation

Target Market(s)

mostly working women

Industry/Entity Type

Fashion

Font styles to use
Serif
Sans Serif

Requirements
Should not have
• butterflies, flowers, feathers, etc

```html
<!DOCTYPE html>
<html lang="en">
<head>
<meta charset="utf-8">
<title>Marta Vosel — Personal Stylist Name Card</title>
<link rel="stylesheet" href="https://fonts.googleapis.com/css2?family=Arimo:wght@700&family=Jost:wght@300&family=Cormorant+SC:wght@600;700&display=swap">
<style>
  :root {
    --page: #e9e7e4;
    --card-light: #3b3b3b;
    --card-dark: #1a1a1a;
    --band: #ffffff;
    --ink-light: #ffffff;
    --ink-dark: #161616;
    --icon-bg: #1e1e1e;
  }
  * { margin: 0; padding: 0; box-sizing: border-box; }
  html, body {
    width: 1200px;
    height: 995px;
    overflow: hidden;
    background: var(--page);
  }
  .sheet {
    width: 1200px;
    height: 995px;
    display: flex;
    flex-direction: column;
    align-items: center;
    justify-content: center;
    gap: 40px;
  }
  .card {
    position: relative;
    width: 800px;
    height: 440px;
    background: radial-gradient(ellipse at 45% 40%, var(--card-light) 0%, #2a2a2a 55%, var(--card-dark) 100%);
    box-shadow: 0 6px 18px rgba(0, 0, 0, 0.25);
    overflow: hidden;
  }
  .band {
    position: absolute;
    left: 0;
    right: 0;
    top: 318px;
    height: 44px;
    background: var(--band);
    display: flex;
    align-items: center;
    font-family: "Cormorant SC", "Times New Roman", serif;
    font-weight: 700;
    color: var(--ink-dark);
    font-size: 24px;
    letter-spacing: 0.02em;
    white-space: nowrap;
  }
  /* Back */
  .card--back .band { justify-content: flex-end; padding-right: 28px; }
  .services .divider { margin: 0 8px; font-weight: 600; }
  /* Front */
  .identity {
    position: absolute;
    left: 38px;
    top: 30px;
    color: var(--ink-light);
  }
  .identity__name {
    font-family: "Arimo", Arial, sans-serif;
    font-weight: 700;
    font-size: 66px;
    line-height: 1;
    letter-spacing: -0.01em;
  }
  .identity__role {
    margin-top: 14px;
    font-family: "Jost", "Futura", sans-serif;
    font-weight: 300;
    font-size: 25px;
    letter-spacing: 0.28em;
  }
  .card--front .band { justify-content: center; font-size: 21px; }
  .contact { display: flex; align-items: center; }
  .contact .divider { margin: 0 8px; font-weight: 600; }
  .contact__icon {
    width: 19px;
    height: 19px;
    margin-right: 6px;
    background: var(--icon-bg);
    display: inline-flex;
    align-items: center;
    justify-content: center;
    flex: none;
  }
  .contact__icon svg { width: 13px; height: 13px; display: block; }
</style>
</head>
<body>
<main class="sheet">
  <section class="card card--back" aria-label="Card back">
    <div class="band">
      <p class="services">Wardrobe weeding<span class="divider">|</span>Personal shopping<span class="divider">|</span>Style consultation</p>
    </div>
  </section>

  <section class="card card--front" aria-label="Card front">
    <div class="identity">
      <h1 class="identity__name">Marta Vosel</h1>
      <p class="identity__role">PERSONAL STYLIST</p>
    </div>
    <div class="band">
      <p class="contact">
        <span class="contact__icon" aria-hidden="true">
          <svg viewBox="0 0 16 16"><circle cx="8" cy="8" r="2.6" fill="none" stroke="#fff" stroke-width="1.6"/><path d="M10.6 5.6v3.4c0 1.2 2.4 1.4 2.4-1 0-3-2.2-5.2-5-5.2S2.8 5 2.8 8s2.2 5.2 5.2 5.2c1.2 0 2.2-.3 3-.9" fill="none" stroke="#fff" stroke-width="1.4"/></svg>
        </span>: www.Marta-Vosel.example
        <span class="divider">|</span>
        <span class="contact__icon" aria-hidden="true">
          <svg viewBox="0 0 16 16"><path d="M4.2 2.2l2 2.6-1.2 1.5c.9 1.9 2.4 3.4 4.3 4.4l1.5-1.2 2.6 2-1.3 2.1C7.400 13.400 2.600 8.600 2.200 3.500z" fill="#fff"/></svg>
        </span>: (+65) 482-30857
        <span class="divider">|</span>
        <span class="contact__icon" aria-hidden="true"></span>: Ringthelook
      </p>
    </div>
  </section>
</main>
</body>
</html>
```